Business Card Design for Small Electrical Contractor

I need to update my business card into something a little more modern. We are a small electrical contracting company. We service domestic and commercial places around Sydney. We have 2 logo designs at the moment. I have uploaded both and 2 different sizes to work with.

Industry/Entity Type

Business

Contact Information for Business Card

Leo Hartigan
8/21-23 Birch Rd, Kelsworth 2087
t - (02) 9381 4720
m - 0427 815 903
E - info@hartiganelx.com.au
W - hartiganelx.com.au
ABN: 42 907 551 316

Font styles to use
Sans Serif

Requirements
Must have
• I would also like to see the below fit on somewhere aswell
• - Licensed Electrician
• - Level 2 (Cat 1 & 4)
• - Domestic
• - Commercial
• - Repairs and Installations
• - Data
Nice to have
• Try and keep similar colours as logo
Should not have
• No lightning bolts or light globes. Smart and professional please.

```html
<!DOCTYPE html>
<html lang="en">
<head>
<meta charset="utf-8">
<title>Hartigan Electrical – Business Card</title>
<link rel="stylesheet" href="https://fonts.googleapis.com/css2?family=Montserrat:wght@400;500;600;700&display=swap">
<style>
  :root {
    --orange: #f39a1e;
    --ink: #1f2a2a;
    --card-black: #0b0b0b;
    --paper: #ffffff;
    --stage: #e6e6e4;
    --muted: #3c4545;
  }
  * { box-sizing: border-box; margin: 0; padding: 0; }
  html, body { width: 1200px; height: 873px; overflow: hidden; }
  body {
    background: var(--stage);
    font-family: "Montserrat", sans-serif;
    position: relative;
  }
  .card {
    position: absolute;
    top: 278px;
    width: 520px;
    height: 316px;
    border-radius: 4px;
    overflow: hidden;
    box-shadow: 0 8px 22px rgba(0,0,0,.18);
  }
  /* ---------- front ---------- */
  .card-front { left: 50px; background: var(--paper); color: var(--ink); }
  .brand {
    position: absolute; left: 30px; top: 30px;
    display: flex; align-items: center; gap: 10px;
  }
  .brand-mark { width: 14px; height: 14px; background: var(--orange); }
  .brand-name {
    font-size: 24px; font-weight: 600; color: var(--ink); letter-spacing: .5px;
  }
  .abn { position: absolute; left: 30px; top: 70px; font-size: 10px; color: var(--muted); letter-spacing: .3px; }
  .contact {
    position: absolute; right: 28px; top: 112px;
    text-align: right;
  }
  .contact-name { font-size: 18px; font-weight: 700; margin-bottom: 10px; }
  .contact-list { list-style: none; }
  .contact-list li {
    display: flex; justify-content: flex-end; align-items: center; gap: 10px;
    font-size: 15px; line-height: 24px; color: var(--ink);
  }
  .icon { width: 15px; height: 15px; flex: none; }
  .icon path, .icon circle, .icon rect { fill: none; stroke: var(--orange); stroke-width: 2; }
  .icon .solid { fill: var(--orange); stroke: none; }
  .address {
    position: absolute; left: 30px; right: 28px; bottom: 24px;
    display: flex; justify-content: space-between; align-items: center;
    font-size: 14px; color: var(--ink);
  }
  /* ---------- back ---------- */
  .card-back { left: 630px; background: var(--card-black); color: #fff; }
  .bands { position: absolute; inset: 0; }
  .bands polygon { fill: var(--orange); }
  .back-brand {
    position: absolute; left: 0; right: 0; top: 62px;
    display: flex; justify-content: center; align-items: center; gap: 10px;
  }
  .back-brand .brand-name { color: #fff; font-size: 24px; }
  .rule { position: absolute; left: 140px; width: 240px; top: 104px; height: 2px; background: var(--orange); }
  .services { position: absolute; left: 0; right: 0; top: 128px; text-align: center; }
  .services h2 { font-size: 18px; font-weight: 600; margin-bottom: 10px; }
  .services ul { list-style: none; }
  .services li { font-size: 13px; font-weight: 500; line-height: 22px; }
</style>
</head>
<body>

<section class="card card-front" aria-label="Business card front">
  <div class="brand">
    <span class="brand-mark"></span>
    <span class="brand-name">Hartigan Electrical</span>
  </div>
  <p class="abn">ABN: 42 907 551 316</p>

  <div class="contact">
    <p class="contact-name">Leo Hartigan</p>
    <ul class="contact-list">
      <li>(02) 9381 4720
        <svg class="icon" viewBox="0 0 16 16" aria-hidden="true"><path class="solid" d="M3 1h3l1.5 4-2 1.2a8 8 0 0 0 4.3 4.3L11 8.5l4 1.5v3a2 2 0 0 1-2 2A12 12 0 0 1 1 3a2 2 0 0 1 2-2z"/></svg></li>
      <li>0427 815 903
        <svg class="icon" viewBox="0 0 16 16" aria-hidden="true"><rect x="4" y="1" width="8" height="14" rx="1.5"/></svg></li>
      <li>info@hartiganelx.com.au
        <svg class="icon" viewBox="0 0 16 16" aria-hidden="true"><rect x="1" y="3" width="14" height="10" rx="1"/><path d="M1 3l7 6 7-6"/></svg></li>
      <li>hartiganelx.com.au
        <svg class="icon" viewBox="0 0 16 16" aria-hidden="true"><circle cx="8" cy="8" r="6.5"/><path d="M1.5 8h13M8 1.5c-3 3.5-3 9.5 0 13M8 1.5c3 3.5 3 9.5 0 13"/></svg></li>
    </ul>
  </div>

  <div class="address">
    <span>8/21-23 Birch Rd, Kelsworth 2087</span>
    <svg class="icon" viewBox="0 0 16 16" aria-hidden="true"><path class="solid" d="M8 0a5.5 5.5 0 0 1 5.5 5.5C13.5 10 8 16 8 16S2.5 10 2.5 5.5A5.5 5.5 0 0 1 8 0zm0 3a2.5 2.5 0 1 0 0 5 2.5 2.5 0 0 0 0-5z"/></svg>
  </div>
</section>

<section class="card card-back" aria-label="Business card back">
  <svg class="bands" viewBox="0 0 520 316" aria-hidden="true">
    <polygon points="0,0 520,0 520,20 150,20 120,8 0,8"/>
    <polygon points="0,316 520,316 520,308 400,308 370,296 0,296"/>
  </svg>
  <div class="back-brand">
    <span class="brand-name">Hartigan Electrical</span>
  </div>
  <div class="rule"></div>
  <div class="services">
    <h2>Licensed Electrician</h2>
    <ul>
      <li>• Level 2 (Cat 1 &amp; 4)</li>
      <li>• Domestic &nbsp;• Commercial</li>
      <li>• Repairs and Installations &nbsp;• Data</li>
    </ul>
  </div>
</section>

</body>
</html>
```